Design eBook Cover for Homeowner Association (HOA) book

We need a cover design for an eBook entitled "The Civic Panel Volunteer's Primer: Self-Direction Hints and Sound Routines".

Title: The Civic Panel Volunteer's Primer

Subtitle: Self-Direction Hints and Sound Routines

Name of Author: Gary Pellston, CMA

Style: Professional Guide

Testimonial: "This book is an indispensable tool for anyone on an HOA board. The expert advice and practical approach in 'The Civic Panel Volunteer's Primer' have made a world of difference in our community. Every board member should have a copy!"
— Wanda Orr, HOA Board President

I have uploaded a file as design inspiration but not locked into the colors or look. Just want a clean, professional looking cover.

Target Market(s)

Board members of HOAs (Homeowners associations) in the United States

Industry/Entity Type

Real Estate, HOA

Requirements
Must have
• Clean, professional appearance that conveys authority

```html
<!DOCTYPE html>
<html lang="en">
<head>
<meta charset="utf-8">
<title>The Civic Panel Volunteer's Primer — Cover</title>
<link rel="stylesheet" href="https://fonts.googleapis.com/css2?family=Lato:wght@700&family=Oswald:wght@300;400;700&display=swap">
<style>
  :root {
    --backdrop: #e6e6e6;
    --cover-yellow: #e9c00a;
    --ink: #0b0b0b;
    --paper-white: #f3f1ea;
    --glow-light: #f4dc63;
  }
  * { margin: 0; padding: 0; box-sizing: border-box; }
  html, body {
    width: 1200px;
    height: 800px;
    overflow: hidden;
    background: var(--backdrop);
  }
  .canvas {
    position: relative;
    width: 1200px;
    height: 800px;
  }
  .cover {
    position: absolute;
    left: 400px;
    top: 96px;
    width: 400px;
    height: 608px;
    background: var(--cover-yellow);
    text-align: center;
    color: var(--ink);
  }
  .subtitle {
    position: absolute;
    left: 0;
    right: 0;
    top: 12px;
    font-family: 'Lato', sans-serif;
    font-weight: 700;
    font-size: 13px;
    line-height: 19px;
    letter-spacing: 0.32em;
    text-transform: uppercase;
  }
  .subtitle-accent { color: var(--paper-white); }
  .title-lead {
    position: absolute;
    left: 0;
    right: 0;
    top: 80px;
    font-family: 'Oswald', sans-serif;
    font-weight: 700;
    font-size: 38px;
    line-height: 38px;
  }
  .title-main {
    position: absolute;
    left: 0;
    right: 0;
    top: 112px;
    font-family: 'Oswald', sans-serif;
    font-weight: 700;
    font-size: 148px;
    line-height: 150px;
    letter-spacing: -0.01em;
  }
  .title-tail {
    position: absolute;
    left: 0;
    right: 0;
    top: 253px;
    font-family: 'Oswald', sans-serif;
    font-weight: 700;
    font-size: 24px;
    line-height: 28px;
    letter-spacing: 0.07em;
    text-transform: uppercase;
  }
  .bulb-art {
    position: absolute;
    left: 160px;
    top: 296px;
    width: 88px;
    height: 168px;
    border-radius: 44px 44px 44px 44px / 60px 60px 44px 44px;
    background: radial-gradient(ellipse at 50% 70%, var(--glow-light) 0%, var(--cover-yellow) 75%);
  }
  .author {
    position: absolute;
    left: 0;
    right: 0;
    top: 486px;
    font-family: 'Oswald', sans-serif;
    font-weight: 700;
    font-size: 35px;
    line-height: 40px;
    letter-spacing: 0.09em;
    color: var(--paper-white);
    text-transform: uppercase;
  }
  .testimonial {
    position: absolute;
    left: 36px;
    right: 36px;
    top: 535px;
    font-family: 'Oswald', sans-serif;
    font-weight: 300;
    font-size: 10px;
    line-height: 12px;
  }
  .testimonial-source {
    display: block;
    font-weight: 700;
    font-style: italic;
  }
</style>
</head>
<body>
  <main class="canvas">
    <section class="cover" aria-label="Book cover">
      <p class="subtitle">
        Self-Direction<br>
        Hints and Sound <span class="subtitle-accent">Routines</span>
      </p>
      <h1>
        <span class="title-lead">THE</span>
        <span class="title-main">CIVIC</span>
        <span class="title-tail">Panel Volunteer's Primer</span>
      </h1>
      <div class="bulb-art" role="img" aria-label="White line drawing of a hanging light bulb on a cord"></div>
      <p class="author">Gary Pellston, CMA</p>
      <blockquote class="testimonial">
        "This book is an indispensable tool for anyone on an HOA board. The expert advice and practical approach in 'The Civic Panel Volunteer's Primer' have made a world of difference in our community. Every board member should have a copy!"
        <cite class="testimonial-source">— Wanda Orr, HOA Board President</cite>
      </blockquote>
    </section>
  </main>
</body>
</html>
```